Overview of Elder Abuse Resources Brochure

We need a 2-page brochure that provides a list of resources for elders in tribal communities in the US and those who care for them. We want it to be simple and easy to read, and easy to see the difference between each resource. We would also like eye-catching images or graphics. Please keep the images on the front, and add any photos or graphics that depict Native American elders. We need both of our logos on the first page, in the far-right column. Please refer to the attached image for our brand colors and a font suggestion. Please keep the three columns on each page, but delete the blank pages in the document.

```html
<!DOCTYPE html>
<html lang="en">
<head>
<meta charset="utf-8">
<title>Services for Elders Brochure</title>
<link href="https://fonts.googleapis.com/css2?family=Barlow+Condensed:wght@500;600;700;800&family=Lato:wght@400;700&display=swap" rel="stylesheet">
<style>
:root{
  --terracotta:#b25b51;
  --navy:#10293a;
  --teal:#3f9ba4;
  --ink:#1f2a33;
  --white:#ffffff;
  --paper:#f4f4f4;
  --photo-warm:#7a3a2c;
}
*{margin:0;padding:0;box-sizing:border-box}
html,body{width:1200px;height:493px;overflow:hidden;background:var(--white)}
body{position:relative;font-family:'Lato',sans-serif;color:var(--ink)}
.page{position:absolute;top:36px;width:544px;height:421px;display:flex;box-shadow:0 0 3px rgba(0,0,0,.25)}
.page--inside{left:37px}
.page--outside{left:619px}
.panel{position:relative;width:181.33px;height:100%;overflow:hidden}
.panel--white{background:var(--white)}
.panel--terracotta{background:var(--terracotta);color:var(--white)}
.panel--navy{background:var(--navy);color:var(--white)}
.abs{position:absolute;left:15px;right:12px}
.heading{font-family:'Barlow Condensed',sans-serif;font-weight:700;font-size:11.5px;line-height:1.05;text-transform:uppercase;letter-spacing:-.1px}
.heading::after{content:"";display:block;width:43px;height:1.6px;margin-top:6px;background:currentColor}
.panel--white .heading::after{background:var(--terracotta)}
.bullets{list-style:none;font-size:6.8px;line-height:1.55}
.bullets li{position:relative;padding-left:14px;margin-bottom:3px;text-align:justify}
.bullets li::before{content:"";position:absolute;left:1px;top:3px;width:4.5px;height:4.5px;border-radius:50%;background:var(--teal)}
.help-text{text-align:center;font-size:10.5px}
.help-phone{text-align:center;font-family:'Barlow Condensed',sans-serif;font-weight:700;font-size:17px;color:var(--teal);letter-spacing:.3px}
.photo{position:absolute}
.photo--elder-seated{left:0;right:0;top:250px;bottom:0;background:linear-gradient(180deg,#fff 0%,#c9aea0 18%,#8e5a48 50%,#6a2f2a 100%)}
.photo--elder-portrait{left:181.33px;width:362.67px;top:70px;height:201px;background:linear-gradient(100deg,#cfc3b8 0%,#8f6c5a 28%,#5a2e24 55%,#8a2f2a 80%,#3a2320 100%)}
.resource{position:absolute;left:11px;right:8px;display:flex;gap:9px}
.icon{flex:0 0 33px;width:33px;height:33px;display:flex;align-items:center;justify-content:center}
.icon svg{width:20px;height:20px;fill:none;stroke:currentColor;stroke-width:1.3;stroke-linecap:round;stroke-linejoin:round}
.icon--navy{background:var(--navy);color:var(--white)}
.icon--terracotta{background:var(--terracotta);color:var(--white)}
.res-title{font-family:'Barlow Condensed',sans-serif;font-weight:700;font-size:9px;line-height:1.05;margin-bottom:2px}
.panel--navy .res-title{color:var(--teal)}
.res-meta{font-size:5.7px;line-height:1.45}
.res-line{display:flex;gap:4px;align-items:flex-start}
.res-line svg{flex:0 0 5px;width:5px;height:5px;margin-top:1.2px;fill:none;stroke:currentColor;stroke-width:1.6}
.res-note{font-size:5.7px;line-height:1.35;margin-top:3px;text-align:justify}
.divider{position:absolute;left:5px;right:5px;height:.6px;background:rgba(255,255,255,.25)}
.sub-heading{font-family:'Barlow Condensed',sans-serif;font-weight:500;font-size:9.5px;color:var(--terracotta)}
.sub-heading--teal{color:var(--teal);font-weight:600}
.kinship{font-family:'Barlow Condensed',sans-serif;font-weight:500;font-size:9.5px;line-height:1.2}
.body-copy{font-size:6.8px;line-height:1.6;text-align:justify}
.body-copy .placeholder{color:var(--terracotta)}
.contact-item{position:absolute;left:15px;right:6px;display:flex;gap:8px;align-items:flex-start}
.contact-item .icon{flex-basis:33px}
.contact-label{font-size:6.6px;line-height:1.5;color:#444;padding-top:1px}
.contact-number{font-family:'Barlow Condensed',sans-serif;font-weight:700;font-size:9px;color:var(--teal);margin-top:2px}
.center{text-align:center;left:8px;right:8px}
.center .heading::after{margin:5px auto 0}
.address{font-size:7px;line-height:1.55;text-align:center}
.accent-strip{position:absolute;left:181.33px;width:362.67px;top:67px;height:3px;background:var(--teal)}
.mailing-block{position:absolute;left:181.33px;width:181.33px;top:0;height:67px;background:var(--terracotta);color:var(--white)}
.org-block{position:absolute;left:181.33px;width:181.33px;top:271px;bottom:0;background:var(--terracotta);color:var(--white)}
.logo-block{position:absolute;left:362.67px;width:181.33px;top:0;height:67px;display:flex;align-items:center;justify-content:center;gap:10px;padding:0 8px}
.logo{display:flex;align-items:center;gap:3px;font-family:'Barlow Condensed',sans-serif;font-weight:700;font-size:7.5px;line-height:1.05;text-transform:uppercase}
.logo--alliance{color:var(--teal)}
.logo--justice{color:#c9a24e}
.logo-mark{width:9px;height:9px;flex:0 0 9px;background:currentColor;border-radius:50%}
.services-block{position:absolute;left:362.67px;width:181.33px;top:271px;bottom:0;background:var(--white)}
.hero-word{position:absolute;left:350px;top:78px;font-family:'Barlow Condensed',sans-serif;font-weight:800;font-size:112px;line-height:1;color:var(--teal);letter-spacing:-2px}
.family-list{position:absolute;left:460px;top:124px;list-style:none;font-family:'Barlow Condensed',sans-serif;font-weight:500;font-size:16px;line-height:22px;color:var(--white)}
.services-title{font-family:'Barlow Condensed',sans-serif;font-weight:700;font-size:17px;line-height:1.05;text-transform:uppercase;color:var(--navy)}
.services-title .accent{color:var(--teal)}
.services-list{list-style:none;font-size:8.4px;line-height:1.2;margin-top:10px}
.services-list li{position:relative;padding-left:14px;margin-bottom:6px}
.services-list li::before{content:"";position:absolute;left:1px;top:3px;width:4.5px;height:4.5px;border-radius:50%;background:var(--terracotta)}
.connect{position:absolute;left:16px;right:6px;display:flex;gap:6px;align-items:center;font-size:5.9px;line-height:1.3}
.round-icon{width:17px;height:17px;flex:0 0 17px;border-radius:50%;background:var(--navy);display:flex;align-items:center;justify-content:center}
.round-icon svg{width:10px;height:10px;fill:none;stroke:var(--white);stroke-width:1.5;stroke-linecap:round;stroke-linejoin:round}
</style>
</head>
<body>

<!-- Inside spread -->
<section class="page page--inside">

  <div class="panel panel--white">
    <div class="abs" style="top:18px;left:15px;right:16px"><h2 class="heading" style="font-size:11.5px">Do these stories sound familiar to you?</h2></div>
    <ul class="bullets abs" style="top:56px;left:15px;right:17px">
      <li>My mother gets lost driving home from the store.</li>
      <li>I need help getting groceries and with chores at home.</li>
      <li>My dad wants to sleep all the time; he doesn't go out with friends anymore. He stopped drumming.</li>
      <li>My sister is raising 3 grandchildren on her own.</li>
      <li>My son is disrespecting me. He only comes to visit when my retirement money arrives. He always asks for money.</li>
    </ul>
    <div class="photo photo--elder-seated" role="img" aria-label="Photo of a Native American elder woman seated, wearing a red velvet blouse and turquoise jewelry"></div>
    <p class="help-text abs" style="top:206px">Help is available...</p>
    <p class="help-phone abs" style="top:220px">(000) 000-0000</p>
  </div>

  <div class="panel panel--terracotta">
    <div class="abs" style="top:18px"><h2 class="heading">Resources for Elders</h2></div>

    <div class="resource" style="top:52px">
      <div class="icon icon--navy"><svg viewBox="0 0 20 20"><path d="M10 17s-5-5-5-9a5 5 0 0 1 10 0c0 4-5 9-5 9z"/><circle cx="10" cy="8" r="2"/><path d="M6 17h8"/></svg></div>
      <div>
        <h3 class="res-title">Elder Support Finder</h3>
        <div class="res-meta">
          <div class="res-line"><svg viewBox="0 0 6 6"><circle cx="3" cy="3" r="2.4"/></svg>https://eldersupportfinder.org/home</div>
          <div class="res-line"><svg viewBox="0 0 6 6"><path d="M1 1l1.5 0 .6 1.4-.8.6a3 3 0 0 0 1.7 1.7l.6-.8L6 4.5V6"/></svg>Call or Text: 1-800-555-0142</div>
          <div class="res-line"><svg viewBox="0 0 6 6"><rect x=".5" y="1.2" width="5" height="3.6"/><path d="M.5 1.2L3 3.2l2.5-2"/></svg>Email: help@eldersupportfinder.org</div>
        </div>
        <p class="res-note">For help finding support. Ask about services to Tribal Elders.</p>
      </div>
    </div>
    <div class="divider" style="top:118px"></div>

    <div class="resource" style="top:127px">
      <div class="icon icon--navy"><svg viewBox="0 0 20 20"><circle cx="10" cy="7" r="4"/><path d="M3 14c2 0 4 1 6 1h4M3 17h10l4-3"/></svg></div>
      <div>
        <h3 class="res-title">Memory Care Call Line</h3>
        <div class="res-meta">(24 hours 7 days a week)</div>
        <div class="res-meta res-line" style="margin-top:3px"><svg viewBox="0 0 6 6"><path d="M1 1l1.5 0 .6 1.4-.8.6a3 3 0 0 0 1.7 1.7l.6-.8L6 4.5V6"/></svg>Call 1-800-555-0177</div>
        <p class="res-note">For support for people living with dementia, caregivers, families and the public. Connect with a live person who can provide information, local resources, crisis assistance and emotional support.</p>
      </div>
    </div>
    <div class="divider" style="top:203px"></div>

    <div class="resource" style="top:212px">
      <div class="icon icon--navy"><svg viewBox="0 0 20 20"><rect x="2" y="4" width="11" height="8" rx="2"/><path d="M5 12l-1 3 3-3"/><rect x="8" y="8" width="10" height="7" rx="2"/></svg></div>
      <div>
        <h3 class="res-title">Talk Now Crisis Line</h3>
        <p class="res-meta">For mental health support,<br>call or text 555-0198.</p>
      </div>
    </div>
    <div class="divider" style="top:249px"></div>

    <div class="resource" style="top:258px">
      <div class="icon icon--navy"><svg viewBox="0 0 20 20"><path d="M10 2l6 2.5v5c0 4-3 6.5-6 8-3-1.5-6-4-6-8v-5z"/><path d="M7 10l2 2 4-4"/></svg></div>
      <div>
        <h3 class="res-title">State &amp; Tribal Hotlines | Elder Justice Network</h3>
        <p class="res-note" style="margin-top:1px">To find local resources within your tribe or state that specialize in elder abuse, neglect or exploitation, visit:</p>
        <div class="res-meta res-line" style="margin-top:3px"><svg viewBox="0 0 6 6"><circle cx="3" cy="3" r="2.4"/></svg>https://agingalliance.org/ejn/hotlines-codes/ state-tribal-hotlines/</div>
      </div>
    </div>
    <div class="divider" style="top:326px"></div>

    <div class="resource" style="top:335px">
      <div class="icon icon--navy"><svg viewBox="0 0 20 20"><path d="M10 17L3 10a4 4 0 0 1 7-5 4 4 0 0 1 7 5z"/><path d="M6 11l3 3 4-4"/></svg></div>
      <div>
        <h3 class="res-title">Circle of Hearts Helpline</h3>
        <p class="res-note" style="margin-top:1px">A 24/7 safe, confidential and anonymous domestic and sexual violence helpline for Native Americans and Alaska Natives.</p>
        <div class="res-meta" style="margin-top:3px">
          <div class="res-line"><svg viewBox="0 0 6 6"><circle cx="3" cy="3" r="2.4"/></svg>https://circleofhearts-help.org/</div>
          <div class="res-line" style="margin-top:3px"><svg viewBox="0 0 6 6"><path d="M1 1l1.5 0 .6 1.4-.8.6a3 3 0 0 0 1.7 1.7l.6-.8L6 4.5V6"/></svg>Call 1-844-555-0163<br>(1-844-555-HELP)</div>
        </div>
      </div>
    </div>
  </div>

  <div class="panel panel--navy">
    <div class="abs" style="top:18px"><h2 class="heading">Resources for Caregivers</h2></div>
    <p class="sub-heading abs" style="top:50px">Caring for an Older Adult</p>

    <div class="resource" style="top:73px">
      <div class="icon icon--terracotta"><svg viewBox="0 0 20 20"><path d="M10 17s-5-5-5-9a5 5 0 0 1 10 0c0 4-5 9-5 9z"/><circle cx="10" cy="8" r="2"/><path d="M6 17h8"/></svg></div>
      <div>
        <h3 class="res-title">Elder Support Finder</h3>
        <div class="res-meta">
          <div class="res-line"><svg viewBox="0 0 6 6"><circle cx="3" cy="3" r="2.4"/></svg>https://eldersupportfinder.org/home</div>
          <div class="res-line"><svg viewBox="0 0 6 6"><path d="M1 1l1.5 0 .6 1.4-.8.6a3 3 0 0 0 1.7 1.7l.6-.8L6 4.5V6"/></svg>Call or Text: 1-800-555-0142</div>
          <div class="res-line"><svg viewBox="0 0 6 6"><rect x=".5" y="1.2" width="5" height="3.6"/><path d="M.5 1.2L3 3.2l2.5-2"/></svg>Email: help@eldersupportfinder.org</div>
        </div>
        <p class="res-note">For help finding support. Ask about services to Tribal Elders.</p>
      </div>
    </div>

    <div class="resource" style="top:148px">
      <div class="icon icon--terracotta"><svg viewBox="0 0 20 20"><circle cx="10" cy="7" r="4"/><path d="M3 14c2 0 4 1 6 1h4M3 17h10l4-3"/></svg></div>
      <div>
        <h3 class="res-title">Memory Friends | Indigenous Aging Alliance</h3>
        <div class="res-meta res-line" style="margin-top:3px"><svg viewBox="0 0 6 6"><circle cx="3" cy="3" r="2.4"/></svg>https://agingalliance.org/memory-friends/</div>
        <p class="res-note" style="margin-top:5px">An interactive educational program to better understand what dementia is and how it affects people.</p>
      </div>
    </div>
    <div class="divider" style="top:224px"></div>

    <p class="sub-heading abs" style="top:236px">Caring for a Grandchild</p>
    <p class="kinship abs" style="top:249px">Grandparents Raising Grandchildren (Kinship Care)</p>

    <div class="resource" style="top:290px">
      <div class="icon icon--terracotta"><svg viewBox="0 0 20 20"><circle cx="10" cy="10" r="8"/><circle cx="7" cy="8" r="1.6"/><circle cx="13" cy="8" r="1.6"/><circle cx="10" cy="11" r="1.4"/><path d="M4.5 13c1-1.5 4-1.5 5 0M10.5 13c1-1.5 4-1.5 5 0"/></svg></div>
      <div>
        <h3 class="res-title">Grandkin.org</h3>
        <p class="res-note" style="margin-top:1px">An interactive website that seeks to share all relevant publicly available information impacting grandfamilies.</p>
      </div>
    </div>

    <div class="resource" style="top:346px">
      <div class="icon icon--terracotta"><svg viewBox="0 0 20 20"><circle cx="7" cy="9" r="3.5"/><circle cx="14" cy="11" r="3"/><path d="M2 17c1-3 9-3 10 0M10 17c1-2 7-2 8 0"/></svg></div>
      <div>
        <h3 class="res-title">Grandparent Resources | Elder Justice Network</h3>
        <p class="res-note" style="margin-top:1px">A list of resources for grandparents raising grandchildren.</p>
        <div class="res-meta res-line" style="margin-top:3px"><svg viewBox="0 0 6 6"><circle cx="3" cy="3" r="2.4"/></svg>https://agingalliance.org/ejn/resource/grand-parent-resources/</div>
      </div>
    </div>
  </div>
</section>

<!-- Outside spread -->
<section class="page page--outside">

  <div class="panel panel--white">
    <div class="abs" style="top:18px"><h2 class="heading">Respect for Elders</h2></div>
    <p class="body-copy abs" style="top:45px">Do you have concerns about an Elder, maybe you see that they are not taking care of themselves, or family only comes once a month when the Elder has money?</p>
    <p class="body-copy abs" style="top:94px">Is an Elder telling you that they are not treated with respect or that someone is bothering them? These may be signs of Elder abuse, neglect or exploitation.</p>
    <p class="sub-heading sub-heading--teal abs" style="top:145px">For Help Contact:</p>
    <p class="body-copy abs" style="top:162px;text-align:left">Your Tribal Social Services or Elders Department: <span class="placeholder">insert contact</span> information for your tribal services, law enforcement, etc.</p>

    <div class="contact-item" style="top:205px">
      <div class="icon icon--terracotta"><svg viewBox="0 0 20 20"><path d="M10 2l6 2.5v5c0 4-3 6.5-6 8-3-1.5-6-4-6-8v-5z"/><path d="M7 10l2 2 4-4"/></svg></div>
      <div><p class="contact-label">The Elder Support Finder for information on Adult Protective Services</p><p class="contact-number">1-800-555-0142</p></div>
    </div>
    <div class="contact-item" style="top:261px">
      <div class="icon icon--terracotta"><svg viewBox="0 0 20 20"><path d="M6 15v-4a4 4 0 0 1 8 0v4M4 15h12v2H4zM10 2v2M4 5l1.3 1.3M16 5l-1.3 1.3"/></svg></div>
      <div><p class="contact-label" style="padding-top:6px">If a serious emergency,</p><p class="contact-number">Call 911.</p></div>
    </div>
    <div class="contact-item" style="top:316px">
      <div class="icon icon--terracotta"><svg viewBox="0 0 20 20"><rect x="5" y="3" width="12" height="9" rx="1.5"/><path d="M8 6h6M8 9h4M3 8v7h2v3l3-3h5"/></svg></div>
      <div><p class="contact-label">For mental health support for yourself or an Elder,</p><p class="contact-number">Call or Text 555-0198</p></div>
    </div>
    <div class="contact-item" style="top:372px">
      <div class="icon icon--terracotta"><svg viewBox="0 0 20 20"><path d="M4 3h3l1.5 4-2 1.5a9 9 0 0 0 5 5L13 11.5l4 1.5v3c0 1-1 2-2 2A13 13 0 0 1 2 5c0-1 1-2 2-2zM12 3a5 5 0 0 1 5 5M12 6a2 2 0 0 1 2 2"/></svg></div>
      <div><p class="contact-label" style="padding-top:6px">Family Safety Hotline</p><p class="contact-number">1.800.555.0119</p></div>
    </div>
  </div>

  <div class="panel"></div>
  <div class="panel"></div>

  <div class="mailing-block">
    <div class="abs center" style="top:16px"><h2 class="heading" style="font-size:11px">Mailing Address</h2></div>
    <p class="address abs center" style="top:36px">Recipient Name<br>123 Main Street City, State ZIP Code</p>
  </div>

  <div class="logo-block">
    <div class="logo logo--alliance"><span class="logo-mark"></span>Indigenous<br>Aging Alliance</div>
    <div class="logo logo--justice">Elder Justice<br>Network</div>
  </div>

  <div class="accent-strip"></div>
  <div class="photo photo--elder-portrait" role="img" aria-label="Portrait photo of an elderly Native American woman in a green headscarf and a red patterned blanket"></div>
  <p class="hero-word">MY</p>
  <ul class="family-list">
    <li>Mother</li><li>Father</li><li>Sister</li><li>Grandchild</li><li>self</li>
  </ul>

  <div class="org-block">
    <div class="abs center" style="top:16px"><h2 class="heading" style="font-size:11px">Organization Details</h2></div>
    <p class="address abs center" style="top:40px">Company Name<br>Street Address City, State ZIP Code</p>
    <div class="abs center" style="top:74px"><h2 class="heading" style="font-size:11px">Connect With Us</h2></div>
    <div class="connect" style="top:107px">
      <span class="round-icon"><svg viewBox="0 0 10 10"><circle cx="5" cy="5" r="4"/><path d="M1 5h8M5 1c2 2 2 6 0 8M5 1c-2 2-2 6 0 8"/></svg></span>
      <span>Website<br>www.example.com</span>
      <span class="round-icon" style="margin-left:10px"><svg viewBox="0 0 10 10"><rect x="1" y="2.5" width="8" height="5.5"/><path d="M1 2.5l4 3 4-3"/></svg></span>
      <span>Email<br>info@example.com</span>
    </div>
    <div class="connect" style="top:130px">
      <span class="round-icon"><svg viewBox="0 0 10 10"><path d="M2 1.5h2l.8 2-1 .8a4.5 4.5 0 0 0 2.4 2.4l.8-1 2 .8v2c0 .5-.5 1-1 1A7 7 0 0 1 1 2.5c0-.5.5-1 1-1z"/></svg></span>
      <span>Phone<br>Tel: (000) 000-0000 &nbsp;- &nbsp;Fax: (000) 000-0000</span>
    </div>
  </div>

  <div class="services-block">
    <h1 class="services-title abs" style="top:12px;left:16px;right:6px"><span class="accent">Services for Elders &amp; People</span> who care for them</h1>
    <ul class="services-list abs" style="top:60px;left:15px;right:10px">
      <li>Are you caring for an Elder or a Grandchild?</li>
      <li>Are you an Elder who needs help staying at home?</li>
      <li>These programs and information can be a helpful resource.</li>
    </ul>
  </div>
</section>

</body>
</html>
```